Single-sided business card for restaurant bellwether with new logo made on this site

Business card options with new logo including restaurant name, address, phone number and website. This business card is single-sided only and will be presented at the hostess desk for clients to take. I would like to see options based on a cream card background, a white card background, a yellow card background and a burgundy colored background. It needs to be elegant and traditional.

Target Market(s)

local and international crowd

Industry/Entity Type

restaurant

Contact Information for Business Card

address, website and phone number

Font styles to use
Serif

Colors
EE7325
F08F49
F5BC92
FAE3D3
FDF4ED

Requirements
Must have
• new logo, address, phone number, website
Should not have
• more than three colors

```html
<!DOCTYPE html>
<html lang="es">
<head>
<meta charset="utf-8">
<title>Bellwether – Tarjeta de presentación</title>
<link href="https://fonts.googleapis.com/css2?family=Cinzel:wght@400;500&display=swap" rel="stylesheet">
<style>
  :root {
    --backdrop: #5e4a38;
    --card-yellow: #f2b027;
    --ink-brown: #3b1a14;
  }
  * { margin: 0; padding: 0; box-sizing: border-box; }
  html, body { width: 900px; height: 1200px; overflow: hidden; }
  body {
    background: var(--backdrop);
    position: relative;
    font-family: "Cinzel", "Times New Roman", serif;
    color: var(--ink-brown);
  }
  .business-card {
    position: absolute;
    background: var(--card-yellow);
  }
  .business-card--framed { left: 73px; top: 130px; width: 777px; height: 452px; }
  .business-card--plain { left: 70px; top: 615px; width: 785px; height: 465px; }
  .card-frame {
    position: absolute;
    left: 28px; top: 28px; right: 28px; bottom: 29px;
    border: 2px solid var(--ink-brown);
  }
  .brand-block {
    position: absolute;
    width: 220px;
    display: flex;
    flex-direction: column;
    align-items: center;
  }
  .brand-square {
    width: 110px; height: 110px;
    background: var(--ink-brown);
  }
  .brand-name {
    margin-top: 22px;
    font-size: 25px;
    font-weight: 500;
    letter-spacing: 2px;
    line-height: 1;
    white-space: nowrap;
  }
  .divider {
    position: absolute;
    width: 2px;
    height: 256px;
    background: var(--ink-brown);
  }
  .contact-block {
    position: absolute;
    font-size: 21px;
    line-height: 31.5px;
    letter-spacing: 0.4px;
  }
  .contact-block p { white-space: nowrap; }
  .contact-block .reservations { margin-top: 21px; }
  .business-card--framed .brand-block { left: 153px; top: 123px; }
  .business-card--framed .divider { left: 366px; top: 98px; }
  .business-card--framed .contact-block { left: 424px; top: 104px; }
  .business-card--plain .brand-block { left: 153px; top: 126px; }
  .business-card--plain .divider { left: 371px; top: 102px; }
  .business-card--plain .contact-block { left: 429px; top: 108px; }
</style>
</head>
<body>
  <section class="business-card business-card--framed">
    <div class="card-frame"></div>
    <div class="brand-block">
      <div class="brand-square"></div>
      <div class="brand-name">BELLWETHER</div>
    </div>
    <div class="divider"></div>
    <div class="contact-block">
      <p>Restaurant Bellwether</p>
      <p>Jacaranda 418</p>
      <p>Bahías de Huatulco,</p>
      <p>Oaxaca CP 70987</p>
      <p class="reservations">Reservaciones</p>
      <p>958-555-0142</p>
      <p>www.bellwether.com.mx</p>
    </div>
  </section>

  <section class="business-card business-card--plain">
    <div class="brand-block">
      <div class="brand-square"></div>
      <div class="brand-name">BELLWETHER</div>
    </div>
    <div class="divider"></div>
    <div class="contact-block">
      <p>Restaurant Bellwether</p>
      <p>Jacaranda 418</p>
      <p>Bahías de Huatulco,</p>
      <p>Oaxaca CP 70987</p>
      <p class="reservations">Reservaciones</p>
      <p>958-555-0142</p>
      <p>www.bellwether.com.mx</p>
    </div>
  </section>
</body>
</html>
```